Business Card Design Project

I have attached the logo and the colour pallete for the branding for the company.

Creative designs for business cards are needed.

The Company is modern corporate.

Industry/Entity Type

Business

```html
<!DOCTYPE html>
<html lang="en">
<head>
<meta charset="utf-8">
<title>Business Card – Front and Back</title>
<link rel="stylesheet" href="https://fonts.googleapis.com/css2?family=Exo+2:wght@800&family=Jost:wght@400;500;600&display=swap">
<style>
  :root {
    --bg-top: #e8eaeb;
    --bg-bottom: #a9b5b4;
    --plum-dark: #2e0f3f;
    --plum: #46164d;
    --plum-light: #4d2057;
    --orange: #f26a33;
    --paper: #f4f3f0;
    --title-grey: #6e6470;
    --ink-light: #f1e9f2;
  }
  * { box-sizing: border-box; margin: 0; padding: 0; }
  html, body { width: 1200px; height: 960px; overflow: hidden; }
  body {
    background: linear-gradient(180deg, var(--bg-top) 0%, var(--bg-bottom) 100%);
    font-family: "Jost", sans-serif;
    position: relative;
  }
  .card {
    position: absolute;
    left: 350px;
    width: 500px;
    height: 286px;
    overflow: hidden;
    box-shadow: 0 6px 18px rgba(40, 30, 50, 0.18);
  }
  /* Front */
  .card--front {
    top: 150px;
    background: radial-gradient(circle at 75% 30%, var(--plum-light) 0%, var(--plum) 45%, var(--plum-dark) 100%);
    display: flex;
    align-items: center;
    justify-content: center;
  }
  .brand {
    font-family: "Jost", sans-serif;
    font-weight: 600;
    letter-spacing: -0.5px;
    display: flex;
    align-items: center;
    gap: 8px;
  }
  .brand__dot {
    border-radius: 50%;
    background: var(--orange);
  }
  .card--front .brand { font-size: 52px; color: #ffffff; }
  .card--front .brand__dot { width: 16px; height: 16px; }

  /* Back */
  .card--back {
    top: 500px;
    background: var(--paper);
  }
  .holder {
    position: absolute;
    left: 42px;
    top: 28px;
  }
  .holder__name {
    font-family: "Exo 2", sans-serif;
    font-weight: 800;
    font-size: 30px;
    color: var(--plum);
    line-height: 1;
  }
  .holder__title {
    font-size: 13px;
    color: var(--title-grey);
    margin-top: 2px;
  }
  .card--back .brand {
    position: absolute;
    right: 14px;
    top: 70px;
    font-size: 24px;
    color: var(--plum);
    gap: 5px;
  }
  .card--back .brand__dot { width: 8px; height: 8px; }
  .contact-panel {
    position: absolute;
    left: 0;
    top: 110px;
    width: 348px;
    height: 176px;
    background: var(--plum);
    padding: 30px 0 0 50px;
  }
  .accent-block {
    position: absolute;
    left: 354px;
    top: 102px;
    width: 140px;
    height: 178px;
    background: var(--orange);
  }
  .contact-list { list-style: none; }
  .contact-list li {
    display: flex;
    align-items: flex-start;
    gap: 12px;
    color: var(--ink-light);
    font-size: 9.5px;
    line-height: 1.3;
    margin-bottom: 6px;
  }
  .contact-list svg { flex: none; width: 12px; height: 12px; margin-top: 1px; }
  .website {
    margin-top: 4px;
    margin-left: 24px;
    font-size: 14px;
    font-weight: 500;
    color: var(--orange);
    letter-spacing: 0.3px;
  }
</style>
</head>
<body>

<section class="card card--front" aria-label="Card front">
  <div class="brand"><span>routewise</span><span class="brand__dot"></span></div>
</section>

<section class="card card--back" aria-label="Card back">
  <div class="holder">
    <div class="holder__name">Your Name</div>
    <div class="holder__title">Title</div>
  </div>
  <div class="brand"><span>routewise</span><span class="brand__dot"></span></div>

  <div class="contact-panel">
    <ul class="contact-list">
      <li>
        <svg viewBox="0 0 12 12"><path d="M6 0.5a3.8 3.8 0 0 0-3.8 3.8C2.2 7 6 11.5 6 11.5S9.8 7 9.8 4.3A3.8 3.8 0 0 0 6 0.5zm0 5.3a1.5 1.5 0 1 1 0-3 1.5 1.5 0 0 1 0 3z" fill="#f26a33"/></svg>
        <span>Address , Street no 1234 , Quarter no 1234<br>City ,State , Country , PIN no 123456</span>
      </li>
      <li>
        <svg viewBox="0 0 12 12"><circle cx="6" cy="6" r="5.4" fill="none" stroke="#f26a33" stroke-width="1"/><path d="M4.2 3.2l1 1-.6.8c.4.8 1 1.4 1.8 1.8l.8-.6 1 1-.7.9C5.5 8 4 6.5 3.3 4.5z" fill="#f26a33"/></svg>
        <span>011-123-4567</span>
      </li>
      <li>
        <svg viewBox="0 0 12 12"><rect x="0.5" y="2.5" width="11" height="7.5" fill="#b9708a"/><path d="M0.5 2.5L6 7l5.5-4.5" fill="none" stroke="#46164d" stroke-width="0.9"/></svg>
        <span>emailaddress@website.com</span>
      </li>
    </ul>
    <div class="website">Yourwebsite.com</div>
  </div>
  <div class="accent-block"></div>
</section>

</body>
</html>
```